College Admissions Consulting needs a small street facing sign for new office location.

I need a graphic design to be used inside window for a banner/sign in office location on a high walking traffic city street, for my company, Campus Lantern. I work with high school students and families on the college planning and selection application process. Please check out the website to learn more about what I do (www.mycampuslantern.example). The banner will be used to market our services at our office location. The final design should utilize logo colors, phone number, and website/email information. I'd like to incorporate a my picture in someway because of face recognition. To be printed on a posterboard or vinyl banner.

Target Market(s)

Parents of high school aged children.

Industry/Entity Type

Education

Font styles to use
Sans Serif

Colors
abd037

Requirements
Must have
• Clean, attractive, and professional design. Attract the attention of people walking by. Information must be clear and readable (phone/email, etc.).
Nice to have
• Utilize the picture with crossed arms (without the brown background on picture).
Emphasize tagline:
Mastering The College Admission Process
....with personalized, professional guidance in planning, selecting, and applying to the right colleges.

```html
<!DOCTYPE html>
<html lang="en">
<head>
<meta charset="utf-8">
<title>Campus Lantern – Window Banner</title>
<link rel="stylesheet" href="https://fonts.googleapis.com/css2?family=Montserrat:wght@600;700&family=Questrial&display=swap">
<style>
  :root {
    --charcoal: #555457;
    --green: #8cc63f;
    --green-light: #c3e3a0;
    --white: #ffffff;
    --orange: #f7a11a;
    --blue: #1a9ad6;
    --photo-dark: #141414;
    --photo-mid: #2a2a2a;
  }
  html, body {
    margin: 0;
    padding: 0;
    width: 1200px;
    height: 800px;
    overflow: hidden;
    background: var(--white);
  }
  .banner {
    position: relative;
    width: 1200px;
    height: 800px;
    overflow: hidden;
    font-family: "Questrial", sans-serif;
    color: var(--charcoal);
  }
  .banner__shapes,
  .portrait {
    position: absolute;
    inset: 0;
  }
  .headline {
    position: absolute;
    top: 34px;
    left: 0;
    width: 960px;
    margin: 0;
    text-align: center;
    font-family: "Montserrat", sans-serif;
    font-weight: 600;
    font-size: 72px;
    line-height: 96px;
    letter-spacing: 0;
    color: var(--white);
  }
  .subline {
    position: absolute;
    top: 288px;
    left: 0;
    width: 960px;
    margin: 0;
    text-align: center;
    font-size: 44px;
    line-height: 49px;
    color: var(--charcoal);
  }
  .brand {
    position: absolute;
    left: 94px;
    top: 536px;
    display: flex;
    align-items: center;
    gap: 16px;
  }
  .brand__dot {
    width: 60px;
    height: 60px;
    border-radius: 50%;
    background: var(--green);
    flex: none;
  }
  .brand__name {
    margin: 0;
    font-size: 40px;
    line-height: 44px;
    color: var(--charcoal);
  }
  .brand__tagline {
    margin: 4px 0 0;
    font-size: 11.5px;
    letter-spacing: 0.6px;
    text-transform: uppercase;
    color: var(--charcoal);
  }
  .contacts {
    position: absolute;
    left: 108px;
    top: 638px;
    margin: 0;
    padding: 0;
    list-style: none;
  }
  .contacts__item {
    display: flex;
    align-items: center;
    height: 44px;
    font-family: "Montserrat", sans-serif;
    font-weight: 600;
    font-size: 30px;
  }
  .contacts__icon {
    width: 34px;
    height: 34px;
    margin-right: 28px;
    flex: none;
  }
  .contacts__item--phone { color: var(--orange); font-weight: 700; font-size: 33px; }
  .contacts__item--email { color: var(--green); }
  .contacts__item--web { color: var(--blue); }
</style>
</head>
<body>
<main class="banner">
  <svg class="banner__shapes" width="1200" height="800" viewBox="0 0 1200 800" aria-hidden="true">
    <defs>
      <linearGradient id="green-field" x1="0" y1="0" x2="1" y2="0.3">
        <stop offset="0" stop-color="#8cc63f"/>
        <stop offset="0.65" stop-color="#95ca4e"/>
        <stop offset="1" stop-color="#c3e3a0"/>
      </linearGradient>
    </defs>
    <rect class="field-green" x="0" y="253" width="1200" height="547" fill="url(#green-field)"/>
    <circle cx="50" cy="330" r="118" fill="#ffffff" opacity="0.1"/>
    <circle cx="490" cy="250" r="120" fill="#ffffff" opacity="0.12"/>
    <circle cx="720" cy="560" r="128" fill="#ffffff" opacity="0.12"/>
    <rect class="band-top" x="0" y="0" width="1200" height="253" fill="var(--charcoal)"/>
    <path class="swoosh" d="M0,512 C260,470 600,492 850,598 L850,800 L0,800 Z" fill="var(--charcoal)"/>
    <path class="panel-white" d="M0,527 C270,488 590,512 840,628 L840,800 L0,800 Z" fill="var(--white)"/>
  </svg>

  <svg class="portrait" width="1200" height="800" viewBox="0 0 1200 800" role="img" aria-label="Portrait of the consultant smiling with arms crossed, wearing a black top">
    <defs>
      <linearGradient id="portrait-tone" x1="0" y1="0" x2="0" y2="1">
        <stop offset="0" stop-color="#2a2a2a"/>
        <stop offset="0.45" stop-color="#141414"/>
        <stop offset="1" stop-color="#141414"/>
      </linearGradient>
    </defs>
    <path d="M940,120 Q962,45 1060,42 Q1170,45 1195,140 L1200,300 L1200,800 L880,800 Q830,700 812,640 Q815,590 860,560 Q930,470 950,400 Q925,330 925,250 Q918,180 940,120 Z" fill="url(#portrait-tone)"/>
  </svg>

  <h1 class="headline">Mastering The College<br>Admission Process</h1>
  <p class="subline">...with personalized, professional guidance<br>in planning, selecting, and applying<br>to the right colleges.</p>

  <div class="brand">
    <span class="brand__dot"></span>
    <div>
      <p class="brand__name">Campus Lantern</p>
      <p class="brand__tagline">Mastering the College Admission Process</p>
    </div>
  </div>

  <ul class="contacts">
    <li class="contacts__item contacts__item--phone">
      <svg class="contacts__icon" viewBox="0 0 24 24" aria-hidden="true"><path fill="var(--orange)" d="M6.6 10.8a15.1 15.1 0 0 0 6.6 6.6l2.2-2.2a1 1 0 0 1 1-.25 11.4 11.4 0 0 0 3.6.57 1 1 0 0 1 1 1V20a1 1 0 0 1-1 1A17 17 0 0 1 3 4a1 1 0 0 1 1-1h3.5a1 1 0 0 1 1 1c0 1.25.2 2.45.57 3.57a1 1 0 0 1-.25 1z"/></svg>
      555-014-PLAN (7526)
    </li>
    <li class="contacts__item contacts__item--email">
      <svg class="contacts__icon" viewBox="0 0 24 24" aria-hidden="true"><rect x="1" y="4" width="22" height="16" rx="1.5" fill="var(--green)"/><path d="M2 5.5 12 13l10-7.5" fill="none" stroke="#ffffff" stroke-width="1.6"/></svg>
      hello@mycampuslantern.example
    </li>
    <li class="contacts__item contacts__item--web">
      <svg class="contacts__icon" viewBox="0 0 24 24" aria-hidden="true"><circle cx="12" cy="12" r="11" fill="var(--blue)"/><g fill="none" stroke="#ffffff" stroke-width="1.4"><ellipse cx="12" cy="12" rx="4.5" ry="11"/><path d="M1 12h22M12 1v22M3 6.5h18M3 17.5h18"/></g></svg>
      www.mycampuslantern.example
    </li>
  </ul>
</main>
</body>
</html>
```